Crazy, Different WOMENS PREWORKOUT Packaging Label

We need a MODERN, CRAZY, FUN packaging preworkout label for WOMEN.
There are no limits for this project, be wild and crazy and DIFFERENT.

The name of the product is VELTANE BLUSH and it is a gym preworkout supplement for women.
The company is called KORVAPLENTIX.

We're looking to convey strength, femininity, uniqueness, health, vitality, vigor, focus, concentration, energy, stamina.

and above all HEALTH
Updates

Project Deadline Extended Reason: Hello All, thanks for your submissions so far. In the interest of receiving the best designs, we will extend the deadline by 5 days. We appreciate your effort and look forward to further revisions to hone and perfect the concepts already submitted. Thank you all for your effort so far! Added Saturday, January 7, 2017

Target Market(s)

Sports Women and Women Gym goers

Font styles to use
Serif
Sans Serif
Decorative
Other font styles liked:
• AR Destine

Requirements
Must have
• It must have SOME red in it somewhere because the product is called VELTANE BLUSH but it does NOT have to be the dominating color.
• It must include our Company logo on the label too, but the company logo and the product name should be harmonious. It should be obvious which part of the design is the company logo and which part is the name of the product.
• Include any one of the Company Logo Strips on the label (see reference files) can make it any color!
Nice to have
• Nice to have something unique and different but appealing to women. but NOT stereotypical of women...
• It should be something strong, elite and feminine BUT NOT bubblegum pink and rainbows...
• The jar is a round white jar.
• Try make it look clean, healthful, effective.
• I'm open to crazy and simple designs.
Should not have
• Should not JUST be pink and purple and stereotypical to women.
• It CAN have pink and purple in it though.

```html
<!DOCTYPE html>
<html lang="en">
<head>
<meta charset="utf-8">
<title>Veltane Blush – Women's Pre-Workout Label</title>
<link rel="stylesheet" href="https://fonts.googleapis.com/css2?family=Bebas+Neue&family=Oswald:wght@500;600&family=Comfortaa:wght@700&family=Roboto+Condensed:wght@500&display=swap">
<style>
  :root {
    --ink-black: #1c1c1e;
    --panel-black: #222224;
    --band-grey: #2e2e31;
    --band-grey-light: #38383b;
    --white: #ffffff;
    --brand-red: #e01f2a;
    --pill-pink: #f0285a;
    --pattern-pink: #ff3d6b;
    --pattern-blue: #c9dcff;
    --silver-light: #f4f6f8;
    --silver-mid: #c4ccd4;
    --silver-dark: #9aa4ae;
    --text-dark: #1a1a1a;
  }
  * { margin: 0; padding: 0; box-sizing: border-box; }
  html, body { width: 1200px; height: 622px; overflow: hidden; background: var(--ink-black); }
  .label { position: relative; width: 1200px; height: 622px; overflow: hidden; background: var(--ink-black); }

  .backdrop { position: absolute; inset: 0; }

  .pattern-strip {
    position: absolute; left: 120px; top: 0; width: 190px; height: 622px;
    background:
      linear-gradient(180deg, rgba(255,61,107,0.35), rgba(201,220,255,0.25), rgba(255,61,107,0.35)),
      #2a2530;
  }

  .company-name {
    position: absolute; left: 0; width: 1384px; top: 128px; text-align: center;
    font-family: "Oswald", sans-serif; font-weight: 600; font-size: 27px; letter-spacing: 1px;
    color: var(--white);
  }
  .company-name .mark {
    display: inline-block; width: 14px; height: 14px; margin-right: 10px;
    background: var(--brand-red); vertical-align: 3px;
  }

  .product-name {
    position: absolute; left: 0; width: 1384px; top: 196px; text-align: center;
    font-family: "Bebas Neue", sans-serif; font-size: 118px; line-height: 1; letter-spacing: 3px;
    color: var(--white);
  }
  .product-name .accent { color: var(--brand-red); }

  .tagline {
    position: absolute; left: 530px; top: 328px;
    font-family: "Oswald", sans-serif; font-weight: 500; font-size: 21px; color: var(--white);
  }

  .info-panel {
    position: absolute; left: 0; top: 0; width: 1200px; height: 622px; pointer-events: none;
  }

  .benefits { position: absolute; left: 430px; top: 455px; width: 300px; list-style: none; }
  .benefits li {
    display: flex; align-items: center; gap: 8px; height: 48px;
    font-family: "Comfortaa", sans-serif; font-weight: 700; font-size: 24px; color: var(--text-dark);
    border-bottom: 1px solid rgba(0,0,0,0.12);
  }
  .benefits li:last-child { border-bottom: none; }
  .benefits li:nth-child(1) { padding-left: 26px; }
  .benefits li:nth-child(2) { padding-left: 38px; }
  .benefits li:nth-child(3) { padding-left: 0; }
  .benefits svg { width: 12px; height: 12px; flex: none; }

  .splash {
    position: absolute; left: 800px; top: 318px; width: 230px; height: 200px;
    border-radius: 60% 40% 30% 70% / 60% 50% 50% 40%;
    background: radial-gradient(ellipse at 60% 55%, rgba(240,80,110,0.9), rgba(255,180,195,0.55) 55%, rgba(255,255,255,0) 75%);
  }

  .flavor-pill {
    position: absolute; left: 774px; top: 514px; width: 262px; height: 48px; border-radius: 8px;
    background: linear-gradient(180deg, #ff4f7a, var(--pill-pink) 60%, #d81c4b);
    display: flex; align-items: center; justify-content: center;
    font-family: "Oswald", sans-serif; font-weight: 600; font-size: 23px; color: var(--white);
  }

  .fine-print {
    position: absolute; left: 774px; top: 570px; width: 266px; display: flex; justify-content: space-between;
    font-family: "Roboto Condensed", sans-serif; font-weight: 500; font-size: 13px; letter-spacing: 1px; color: var(--text-dark);
  }
</style>
</head>
<body>
<main class="label">
  <svg class="backdrop" width="1200" height="622" viewBox="0 0 1200 622" aria-hidden="true">
    <defs>
      <linearGradient id="silver" x1="0" y1="0" x2="1" y2="1">
        <stop offset="0" stop-color="#aeb7c0"/>
        <stop offset="0.3" stop-color="#f4f6f8"/>
        <stop offset="0.55" stop-color="#c4ccd4"/>
        <stop offset="0.8" stop-color="#eef1f4"/>
        <stop offset="1" stop-color="#9aa4ae"/>
      </linearGradient>
    </defs>
    <rect width="1200" height="622" fill="#1f1f21"/>
    <g fill="#2b2b2e">
      <polygon points="0,120 110,40 110,120 0,200"/>
      <polygon points="0,330 110,250 110,330 0,410"/>
      <polygon points="0,540 110,460 110,540 0,620"/>
      <polygon points="1090,100 1200,20 1200,100 1090,180"/>
      <polygon points="1090,310 1200,230 1200,310 1090,390"/>
      <polygon points="1090,520 1200,440 1200,520 1090,600"/>
    </g>
    <rect x="320" y="0" width="744" height="622" fill="#232325"/>
    <g fill="#2f2f32">
      <polygon points="320,0 380,0 692,270 1004,0 1064,0 692,320"/>
      <polygon points="320,170 692,470 1064,170 1064,230 692,530 320,230"/>
    </g>
    <path d="M450,426 L1064,426 L1064,622 L324,622 L436,440 Q442,426 450,426 Z" fill="url(#silver)"/>
  </svg>

  <div class="pattern-strip" role="img" aria-label="Decorative column of pink, pale blue and dark square and diamond tiles"></div>

  <div class="company-name"><span class="mark"></span>KORVAPLENTIX</div>

  <h1 class="product-name">VELTANE <span class="accent">BLUSH</span></h1>
  <p class="tagline">Women's PRE-WORKOUT Formula</p>

  <ul class="benefits">
    <li><svg viewBox="0 0 12 12"><path d="M6 11 L1 6 A2.6 2.6 0 0 1 6 2.5 A2.6 2.6 0 0 1 11 6 Z" fill="#1a1a1a"/></svg>increased energy</li>
    <li><svg viewBox="0 0 12 12"><path d="M6 11 L1 6 A2.6 2.6 0 0 1 6 2.5 A2.6 2.6 0 0 1 11 6 Z" fill="#1a1a1a"/></svg>ignite fat loss</li>
    <li><svg viewBox="0 0 12 12"><path d="M6 11 L1 6 A2.6 2.6 0 0 1 6 2.5 A2.6 2.6 0 0 1 11 6 Z" fill="#1a1a1a"/></svg>build a lean physeque</li>
  </ul>

  <div class="splash" role="img" aria-label="Pink raspberry lemonade liquid splash"></div>

  <div class="flavor-pill">RASPBERRY LEMONADE</div>
  <div class="fine-print"><span>DIETARY SUPPLEMENT</span><span>NET WT. 12 OZ</span></div>
</main>
</body>
</html>
```